依頼詳細
現在使っているものを画像データで添付します。
事務所ロゴをフォトショップデータで添付します。

参考に、市販の表紙デザインにはこういったものがあります。(下記リンク)
https://www.kazane-dk.co.jp/store/products/list.php?category_id=23
https://tomoriworks.com/item/certificate/
http://mizuho-kanade.com/front_cover/
A4の紙を綴じるものなので、A3より一回り大きいA3ワイドのレザック紙に印刷しております。こちら302×430mmサイズです。

表紙には、お客様(権利者)の名前と
その下には不動産の表示が入ります。(案件ごとに印刷します)
そのため、こちらを手差し印刷できるよう、高さ5センチ程度の空白を空けておいていただきたいです。

サイズ:A3ワイド(302×430mm)
2つ折り、左開きです。半分に折った部分が表紙となります。

色、デザインの雰囲気等お任せいたします。
公的で固い重要書類をいれるものですが、そういったイメージにはあまり縛られずなるべくオリジナリティのあるものを使いたいと思います。
記載項目
不動産登記権利情報

司法書士ふじさわ事務所
希望イメージ
シンプル 複雑
単色 カラフル
暗い 明るい
日常 高級
遊び心 厳粛
未来的 伝統的
女性的 男性的
希望する色
設定なし
納品ファイル
• イラストレーター形式 (.ai)
補足説明
設定なし
【追記】桐のマークについて
現在使っている権利証表紙には、司法書士バッヂの意匠である五三桐花をいれておりますが、今回は特に使用の指定はしません。
桐のマークを入れる場合については、五三桐でお願いいたします(葉っぱが中央に5枚・左右に3枚ずつの家紋)

(参考)
http://senra-mokudo.com/kamon-c/cate0/kiri/kiri2.html
https://www.ezukan-store.jp/img344/225970_3130817.html
■ 選んだ理由

見た瞬間に目を惹くデザインだと思い、選ばせていただきました。

■ 提案者全員のお礼・コメント

たくさんのご提案をいただき大変嬉しく思っております。
皆様それぞれ、素敵なデザインを考えていただき本当にありがとうございます。

```html
<!DOCTYPE html>
<html lang="ja">
<head>
<meta charset="utf-8">
<title>不動産登記権利情報 表紙</title>
<link rel="stylesheet" href="https://fonts.googleapis.com/css2?family=Shippori+Mincho:wght@500;700&display=swap">
<style>
  :root {
    --paper: #ffffff;
    --page-line: #a9d3e6;
    --frame-band: #b9dde9;
    --frame-inner: #d9eef5;
    --panel: #c6e4ee;
    --ornament: #e9f5f9;
    --ink: #1f3f8f;
    --rule: #2a55b0;
    --slot: #ffffff;
  }
  html, body {
    margin: 0;
    padding: 0;
    width: 859px;
    height: 1200px;
    overflow: hidden;
    background: var(--paper);
  }
  .cover {
    position: relative;
    width: 859px;
    height: 1200px;
    background: var(--paper);
    font-family: "Shippori Mincho", serif;
  }
  .page-edge {
    position: absolute;
    left: 10px; top: 10px; right: 10px; bottom: 10px;
    border: 2px solid var(--page-line);
  }
  .panel {
    position: absolute;
    left: 60px; top: 50px;
    width: 740px; height: 1080px;
    background: var(--frame-band);
  }
  .panel-field {
    position: absolute;
    left: 22px; top: 22px; right: 22px; bottom: 22px;
    background: var(--panel);
    outline: 2px solid var(--frame-inner);
    outline-offset: -6px;
  }
  .corner-ornament {
    position: absolute;
    width: 90px; height: 90px;
    background: var(--ornament);
    opacity: 0.75;
  }
  .corner-ornament.tl { left: 10px; top: 10px; border-radius: 0 0 70px 0; }
  .corner-ornament.tr { right: 10px; top: 10px; border-radius: 0 0 0 70px; }
  .corner-ornament.bl { left: 10px; bottom: 10px; border-radius: 0 70px 0 0; }
  .corner-ornament.br { right: 10px; bottom: 10px; border-radius: 70px 0 0 0; }
  .title {
    position: absolute;
    left: 0; right: 0; top: 222px;
    margin: 0;
    text-align: center;
    font-size: 46px;
    font-weight: 700;
    letter-spacing: 2px;
    color: var(--ink);
  }
  .title-rule {
    position: absolute;
    left: 190px; width: 360px;
    top: 312px; height: 4px;
    background: var(--rule);
  }
  .print-slot {
    position: absolute;
    left: 195px; width: 350px;
    height: 72px;
    background: var(--slot);
    border-radius: 22px;
  }
  .print-slot.holder { top: 464px; }
  .print-slot.property { top: 558px; }
  .slot-divider {
    position: absolute;
    left: 195px; width: 350px;
    top: 545px; height: 3px;
    background: var(--rule);
  }
  .office-mark {
    position: absolute;
    left: 318px; top: 790px;
    width: 104px; height: 104px;
    background: var(--slot);
    border-radius: 14px;
  }
  .office-name {
    position: absolute;
    left: 0; right: 0; top: 950px;
    margin: 0;
    text-align: center;
    font-size: 30px;
    font-weight: 500;
    color: var(--ink);
  }
</style>
</head>
<body>
  <main class="cover">
    <div class="page-edge"></div>
    <section class="panel">
      <div class="panel-field">
        <div class="corner-ornament tl" role="img" aria-label="角の唐草飾り"></div>
        <div class="corner-ornament tr" role="img" aria-label="角の唐草飾り"></div>
        <div class="corner-ornament bl" role="img" aria-label="角の唐草飾り"></div>
        <div class="corner-ornament br" role="img" aria-label="角の唐草飾り"></div>
      </div>
      <h1 class="title">不動産登記権利情報</h1>
      <div class="title-rule"></div>
      <div class="print-slot holder"></div>
      <div class="slot-divider"></div>
      <div class="print-slot property"></div>
      <div class="office-mark"></div>
      <p class="office-name">司法書士ふじさわ事務所</p>
    </section>
  </main>
</body>
</html>
```